依頼詳細
★重視する点
60歳~70歳の社長が読むものです。
商品も50万円以上のコンサルティングなので、
信頼感、安心感を与える雰囲気を重視します。
また、高級感のあるイメージも重要です。

★ページ構成について
表面 キャッチ
中面 スキームの説明、Q&A
裏面 報酬、お問合せ先

内容を詰めることができれば、
A4裏表の1枚でもOKです。
(むしろ、そうできればベストです)

★文章の修正について
必要があれば文章やタイトルの修正もOKです。
目的は、
「このような方法があるなら、もっと話しを聞いてみたい」
と思わせることです。
そのように思わせるものであれば、
タイトルや文章の修正も歓迎します。

★お問合せの部分について
数名でこのパンフを共同利用する予定です。
ですから、お問合せの部分は
各自の住所と会社名、電話番号、メールアドレスなどが
入りますので、そのようなスペースを空けておいてください。

★利用用途
このパンフレットは、
問合せがあった人に、最初の相談の時、お渡しします。
またセミナーなど開催したときに、資料としてお渡しします。

★納品形式について
イラストレーターV14で開ける形式でお願いいたします。
また、JpegやPNGもお願いします。
サイズ
A4
ページ数
4ページ
希望イメージ
シンプル 複雑
単色 カラフル
暗い 明るい
日常 高級
遊び心 厳粛
未来的 伝統的
女性的 男性的
希望する色
茶系、グレー系
納品ファイル
• 高解像度JPG (.jpg)
• イラストレーター形式 (.ai)
• PNG形式 (.png)
補足説明
・表面、中面、裏面のラフ案をご提案ください。
こちらの希望するイメージに近い提案を1つ選択させて頂きます。

・希望に近づけるために、修正要望を個別にさせていただくこともあります。
コンペ方式のため、修正後に当選されない場合も、どうかご了承ください。
参加報酬は4件用意していますので、
なるべくそちらで対応するようにいたします。

・今後も同様なものを作成する予定です。
依頼は今回だけではなく、こちらの求める条件に合えば
継続して依頼したいと思います。

・疑問点などございましたらお気軽にご質問ください。
早速に1件のご提案があり、大変ありがとうございます。
さすがプロの方のデザインはすばらしく、
これからの提案もとても期待しております。

★お願い スキームの図解もデザインに盛り込んでください

原案に、自社株信託のスキームの図解がありますが、
できれば、パンフレットにも図解を盛り込んで
いただけないでしょうか?
もちろん、原案のスキームの図を参考に
あなたのイメージするようにデザインし直していただきたいです。

原案がワードで作成したため、マクロウィルスなどご心配の方も
いらっしゃると思いますので、原案のPDFを添付します。
また、スキームの図のPNGも添付します。
図はMSのVisioというソフトで作っております。
開ける人は少ないでしょうが、そのファイルも添付します。
■ 選んだ理由

ビジネスというジャングルを駆け巡る獅子(社長)が
寂しげな目で「引退するか」という表紙は、
提案の中で、圧倒的でした。

また、多くの提案をいただいて、気づいたのですが、
老夫婦だと保険の勧誘、引退をイメージする物だと
投資信託などの金融商品の勧誘のような印象を与えることがわかり、
ライオンの表紙はそのような印象も与えないので、
当選とさせていただきました。

■ 提案者全員のお礼・コメント

多くの方からご応募いただき、誠にありがとうございました。
どの提案も、とても私のような素人ではできない
優れたデザインだったと思います。
さすがプロの仕事を見せていただきました。
また、今後も提案をお願いすると思いますが、
そのときも、よろしくお願いいたします。

この度は大変ありがとうございました。

```html
<!DOCTYPE html>
<html lang="ja">
<head>
<meta charset="utf-8">
<title>自社株信託のご案内</title>
<link href="https://fonts.googleapis.com/css2?family=Noto+Sans+JP:wght@400;500;700;900&family=Noto+Serif+JP:wght@700&display=swap" rel="stylesheet">
<style>
:root{
  --brown:#6b4a2e;
  --brown-dark:#45301d;
  --beige:#ece3d6;
  --beige-soft:#f7f2ec;
  --grey:#7d7a76;
  --grey-line:#cfc7bc;
  --accent:#b5621c;
  --ink:#2b2724;
  --muted:#555049;
  --white:#fff;
  --photo-a:#d6d3cf;
  --photo-b:#8f8a84;
}
*{margin:0;padding:0;box-sizing:border-box}
html,body{width:854px;height:1200px;overflow:hidden;background:var(--white)}
body{font-family:"Noto Sans JP",sans-serif;color:var(--ink);position:relative}

.hero{position:absolute;left:0;top:0;width:854px;height:300px;background:linear-gradient(90deg,#faf7f3 0%,#efe9e1 50%,var(--photo-a) 62%);overflow:hidden}
.hero-photo{position:absolute;right:0;top:0;width:380px;height:300px;background:linear-gradient(160deg,var(--photo-a) 0%,#b1aca6 50%,var(--photo-b) 100%)}
.hero-title{position:absolute;left:44px;top:22px;color:var(--brown);font-family:"Noto Serif JP",serif;font-weight:700;font-size:42px;line-height:1.3;letter-spacing:2px}
.hero-rule{position:absolute;left:44px;top:208px;width:360px;height:2px;background:var(--brown)}
.hero-lead{position:absolute;left:44px;top:220px;color:var(--brown-dark);font-weight:700;font-size:18px;line-height:1.5}

.worry{position:absolute;left:0;top:300px;width:854px;height:180px;background:var(--beige)}
.worry-figure{position:absolute;left:34px;top:10px;width:56px;height:56px;border-radius:50%;background:linear-gradient(#e9d3bd,#cfc4b6)}
.worry-bubble{position:absolute;left:106px;top:14px;width:714px;height:46px;background:var(--white);border:2px solid var(--accent);border-radius:23px;display:flex;align-items:center;padding:0 20px;color:var(--accent);font-weight:700;font-size:14px;white-space:nowrap}
.worry-text{position:absolute;left:34px;top:70px;width:786px;font-size:10.5px;line-height:1.7;color:var(--ink)}
.worry-text b{color:var(--brown)}

.question{position:absolute;left:0;top:480px;width:854px;height:50px;display:flex;align-items:center;padding-left:96px;color:var(--brown);font-weight:700;font-size:15.5px;border-bottom:1px solid var(--grey-line)}
.question-figure{position:absolute;left:36px;top:6px;width:40px;height:38px;border-radius:50%;background:linear-gradient(#e9d3bd,#cfc4b6)}

.define{position:absolute;left:34px;top:538px;width:786px}
.define-tag{display:inline-block;background:var(--brown);color:var(--white);font-weight:700;font-size:13px;padding:3px 14px;border-radius:3px}
.define-list{margin-top:6px;display:grid;grid-template-columns:1fr 1fr;gap:3px 20px;list-style:none;font-size:11px;color:var(--ink)}
.define-list li::before{content:"■ ";color:var(--brown)}

.scheme{position:absolute;left:34px;top:612px;width:786px;height:86px;display:flex;align-items:center;justify-content:space-between}
.scheme-box{width:200px;height:70px;border:2px solid var(--brown);border-radius:6px;background:var(--white);display:flex;flex-direction:column;align-items:center;justify-content:center;text-align:center}
.scheme-role{font-weight:700;font-size:14px;color:var(--brown)}
.scheme-who{font-size:11px;color:var(--muted);margin-top:2px}
.scheme-link{flex:1;display:flex;flex-direction:column;align-items:center;font-size:10.5px;color:var(--grey)}
.scheme-link svg{width:100%;height:14px}

.faq{position:absolute;left:0;top:704px;width:854px;height:424px;background:var(--beige-soft)}
.emblem{position:absolute;left:30px;top:12px;width:212px;height:212px;border-radius:50%;background:var(--white);border:6px solid var(--brown);display:flex;flex-direction:column;align-items:center;justify-content:center;text-align:center}
.emblem-sub{color:var(--accent);font-size:13px;font-weight:700;line-height:1.5}
.emblem-main{font-family:"Noto Serif JP",serif;color:var(--brown-dark);font-size:29px;font-weight:700;line-height:1.2;margin-top:6px}

.qa{position:absolute;background:var(--white);border-radius:6px;padding:9px 14px;box-shadow:0 1px 3px rgba(0,0,0,.12)}
.qa-q{color:var(--brown);font-weight:700;font-size:12.5px;margin-bottom:3px}
.qa-a{font-size:10.5px;line-height:1.6;color:var(--muted)}
.qa-a em{font-style:normal;color:var(--accent);font-weight:700}
.qa-1{left:262px;top:12px;width:562px}
.qa-2{left:262px;top:92px;width:562px}
.qa-3{left:262px;top:172px;width:562px}
.qa-4{left:30px;top:252px;width:390px}
.qa-5{left:434px;top:252px;width:390px}

.contact{position:absolute;left:30px;top:1134px;width:794px;height:58px;border:1.5px dashed var(--grey);border-radius:6px;display:flex;align-items:center;padding:0 18px;gap:24px;font-size:11px;color:var(--grey)}
.contact-title{font-weight:700;font-size:13px;color:var(--brown)}
</style>
</head>
<body>

<header class="hero">
  <div class="hero-photo" role="img" aria-label="窓辺に立つスーツ姿の年配の社長の写真"></div>
  <h1 class="hero-title">社長！<br>そろそろ「隠居」<br>しませんか？</h1>
  <div class="hero-rule"></div>
  <p class="hero-lead">贈与税をかけずに会社の株を<br>後継者に渡す方法があります</p>
</header>

<section class="worry">
  <div class="worry-figure" role="img" aria-label="悩む社長のイラスト"></div>
  <div class="worry-bubble">後継者も決まったし、そろそろ「隠居」したいけど、株の譲渡には多額の税金がかかるし…</div>
  <p class="worry-text">
    会社のオーナーである社長にとって、自社株をどう後継者に引き継ぐかは大きな課題です。生前に株を贈与すると、評価額によっては<b>多額の贈与税</b>がかかります。一方、遺言で相続させる方法では、社長が元気なうちは経営権を渡すことができず、後継者の育成も思うように進みません。さらに、一度渡した株は簡単に取り戻せないため、後継者の経営に不安があっても手の打ちようがありません。<br>
    例えば、評価額3,000万円の株を贈与すると、<b>贈与税はおよそ1,000万円</b>にもなります。この負担を避けつつ、社長の意思を会社に残し、円満に事業を承継する方法はないのでしょうか。
  </p>
</section>

<div class="question">
  <div class="question-figure" role="img" aria-label="考える社長のイラスト"></div>
  では、贈与税もかからず、遺言も不要、しかもいつでも元に戻せる方法があるのでしょうか？
</div>

<section class="define">
  <span class="define-tag">「自社株信託」とは</span>
  <ul class="define-list">
    <li>株の名義を後継者に移しても贈与税がかかりません</li>
    <li>社長が元気なうちに経営を任せることができます</li>
    <li>遺言がなくても確実に株を承継できます</li>
    <li>必要があればいつでも元に戻すことができます</li>
  </ul>
</section>

<section class="scheme" aria-label="自社株信託のしくみ">
  <div class="scheme-box"><p class="scheme-role">委託者</p><p class="scheme-who">社長（株を信託）</p></div>
  <div class="scheme-link">
    <span>株を信託</span>
    <svg viewBox="0 0 100 14" preserveAspectRatio="none"><line x1="6" y1="7" x2="90" y2="7" stroke="#6b4a2e" stroke-width="2"/><polygon points="90,2 99,7 90,12" fill="#6b4a2e"/></svg>
  </div>
  <div class="scheme-box"><p class="scheme-role">受託者</p><p class="scheme-who">後継者（議決権を行使）</p></div>
  <div class="scheme-link">
    <span>配当などの利益</span>
    <svg viewBox="0 0 100 14" preserveAspectRatio="none"><line x1="6" y1="7" x2="90" y2="7" stroke="#6b4a2e" stroke-width="2"/><polygon points="90,2 99,7 90,12" fill="#6b4a2e"/></svg>
  </div>
  <div class="scheme-box"><p class="scheme-role">受益者</p><p class="scheme-who">社長（利益を受け取る）</p></div>
</section>

<section class="faq">
  <div class="emblem">
    <p class="emblem-sub">生前贈与でも、<br>遺言でもない</p>
    <p class="emblem-main">自社株信託<br>とは</p>
  </div>

  <div class="qa qa-1">
    <p class="qa-q">Q 贈与税はかからないのですか？</p>
    <p class="qa-a">信託の設定時には株の利益が社長に残るため、<em>贈与税はかかりません</em>。配当などの利益は社長が受け取り続けられます。</p>
  </div>
  <div class="qa qa-2">
    <p class="qa-q">Q 社長が亡くなったときはどうなりますか？</p>
    <p class="qa-a">信託契約であらかじめ後継者を定めておくので、遺言書がなくても株はスムーズに後継者へ引き継がれます。</p>
  </div>
  <div class="qa qa-3">
    <p class="qa-q">Q 後継者に不安が出たら元に戻せますか？</p>
    <p class="qa-a">契約の内容によって、社長の判断で<em>いつでも信託を終了</em>し、株を手元に戻すことができます。</p>
  </div>
  <div class="qa qa-4">
    <p class="qa-q">Q オーナーに相続が発生したらどうなるの？</p>
    <p class="qa-a">信託の受益権が相続の対象となりますが、経営権はすでに後継者にあるため、会社の運営が止まることはありません。相続税の対策も合わせてご提案します。</p>
  </div>
  <div class="qa qa-5">
    <p class="qa-q">Q 後継者が会社を辞めることになったら？</p>
    <p class="qa-a">信託の内容を変更し、新たな後継者を指定することが可能です。会社を守る仕組みを柔軟に整えることができます。</p>
  </div>
</section>

<aside class="contact" aria-label="お問合せ先記入欄">
  <span class="contact-title">お問合せ先</span>
  <span>会社名</span><span>住所</span><span>電話番号</span><span>メールアドレス</span>
</aside>

</body>
</html>
```